Change of trading name, rebrand

existing website to be updated with new theme and logo. existing website is
www.brackenridgeworks.com.au
Industry/Entity Type
Construction
Coding
Coded - Design and coding required
Number of Pages Required
5+ page
Requirements
Must have
- be mobile phone friendly

```html
<!DOCTYPE html>
<html lang="en">
<head>
<meta charset="utf-8">
<title>BRW Heavy Equipment Hire</title>
<link rel="stylesheet" href="https://fonts.googleapis.com/css2?family=Montserrat:ital,wght@0,400;0,500;0,600;0,700;0,800;1,700&family=Poppins:wght@400;500;600&display=swap">
<style>
:root{
  --purple:#2b1157;
  --purple-deep:#1f0b45;
  --purple-mid:#3d1c73;
  --ink:#111;
  --text:#333;
  --grey-bg:#f2f2f2;
  --white:#fff;
  --footer:#0b0b0b;
}
*{box-sizing:border-box;margin:0;padding:0}
html,body{width:1200px;height:3886px;overflow:hidden}
body{font-family:"Montserrat",sans-serif;color:var(--text);background:var(--white);position:relative}
.abs{position:absolute}

/* header */
.site-header{position:absolute;left:0;top:0;width:1200px;height:110px;border-top:4px solid var(--purple);background:var(--white)}
.brand{position:absolute;left:100px;top:14px;display:flex;align-items:center;gap:10px}
.brand-mark{width:22px;height:22px;background:var(--purple)}
.brand-name{font-weight:800;font-size:34px;color:var(--purple);letter-spacing:1px}
.pill{position:absolute;top:12px;height:40px;border-radius:20px;display:flex;align-items:center;justify-content:center;color:#fff;font-size:15px;font-weight:600}
.pill-phone{left:738px;width:160px;background:var(--purple);gap:10px;font-weight:500}
.pill-quote{left:926px;width:176px;background:var(--ink);font-weight:700;font-size:14px}
.nav-bar{position:absolute;left:282px;top:58px;width:918px;height:52px}
.nav{position:absolute;left:74px;top:58px;height:52px;display:flex;align-items:center;gap:30px;font-size:14.5px;font-weight:500;color:#fff}
.nav .active{text-decoration:underline;text-underline-offset:4px;font-weight:600}

/* hero */
.hero{position:absolute;left:0;top:110px;width:1200px;height:570px;background:linear-gradient(100deg,#4d4a45 0%,#6e665c 35%,#a0907e 60%,#7e8fa8 85%,#a9bdd6 100%)}
.hero h1{position:absolute;left:99px;top:142px;color:#fff;font-size:49px;font-weight:700;line-height:57px;letter-spacing:.5px}
.hero .rule{position:absolute;left:99px;top:275px;width:50px;height:3px;background:#fff}
.hero p{position:absolute;left:99px;top:292px;color:#fff;font-size:17px;line-height:29px;font-weight:500;width:340px}
.hero .btn{position:absolute;left:99px;top:374px;width:153px;height:43px;border-radius:22px;background:#fff;color:var(--purple);font-weight:700;font-size:15.5px;display:flex;align-items:center;justify-content:center}
.scroll-cue{position:absolute;left:588px;top:485px}

/* section titles */
.section-title{position:absolute;left:0;width:1200px;text-align:center}
.section-title .ghost{font-size:74px;font-weight:700;font-style:italic;color:transparent;-webkit-text-stroke:1px #ececec;letter-spacing:2px;line-height:1}
.section-title h2{position:absolute;left:0;width:1200px;font-size:32px;font-weight:700;color:var(--purple);letter-spacing:.5px}
.section-title .bar{position:absolute;left:575px;width:50px;height:4px;background:var(--purple)}

/* who we are */
.features{position:absolute;top:860px;left:0;width:1200px}
.feature{position:absolute;width:200px;text-align:center}
.feature .ico{width:98px;height:98px;border-radius:50%;margin:0 auto;display:flex;align-items:center;justify-content:center}
.feature p{margin-top:20px;font-size:15.5px;font-weight:500;line-height:29px;color:#111}

/* about */
.about{position:absolute;left:0;top:1110px;width:1200px;height:600px;background:linear-gradient(120deg,var(--purple-deep) 0%,var(--purple-mid) 55%,#32175f 100%)}
.about-photo{position:absolute;left:125px;top:92px;width:410px;height:410px;border-radius:50%;background:linear-gradient(180deg,#7aa8e0 0%,#b9d1ea 45%,#b49a5e 62%,#8b6a3a 100%)}
.about-ring{position:absolute;left:130px;top:88px}
.about-text{position:absolute;left:637px;top:80px;width:460px;color:#fff}
.about-text h2{font-size:32px;font-weight:700;letter-spacing:.5px}
.about-text .ghost{position:absolute;left:-10px;top:-10px;font-size:72px;font-weight:700;font-style:italic;color:transparent;-webkit-text-stroke:1px rgba(255,255,255,.22);white-space:nowrap}
.about-text .bar{width:50px;height:4px;background:#fff;margin-top:10px}
.about-text p{font-size:14.5px;line-height:28.5px;margin-top:18px}
.about-text .btn{margin-top:26px;width:133px;height:45px;border-radius:23px;background:#fff;color:var(--purple);font-weight:700;font-size:15px;display:flex;align-items:center;justify-content:center}

/* services */
.card{position:absolute;top:1880px;width:309px;background:#fff;box-shadow:0 4px 14px rgba(0,0,0,.12);text-align:center}
.card .img{height:185px}
.card h3{font-size:17px;font-weight:600;color:#111;margin-top:25px;letter-spacing:.3px}
.card .arrow{width:56px;height:29px;background:#111;margin:25px auto 0;display:flex;align-items:center;justify-content:center}
.card.open{border-bottom:5px solid var(--purple)}
.card.open h3{color:var(--purple)}
.card.open p{font-size:13.5px;line-height:22.5px;color:#222;margin:12px 14px 0}
.card.open .more{display:inline-block;margin:16px 0 30px;font-size:14px;font-weight:700;color:var(--purple);text-decoration:underline;text-underline-offset:3px}
.view-more{position:absolute;left:534px;top:2368px;width:132px;height:47px;border-radius:24px;background:var(--purple);color:#fff;font-weight:700;font-size:15.5px;display:flex;align-items:center;justify-content:center}

/* contact */
.contact{position:absolute;left:0;top:2510px;width:1200px;height:602px;background:var(--grey-bg);overflow:hidden}
.contact h2{position:absolute;left:95px;top:135px;font-size:30px;line-height:44px;font-weight:700;color:var(--purple);letter-spacing:.5px}
.contact .lead{position:absolute;left:101px;top:238px;font-size:14.5px;line-height:26px;color:#333;width:330px}
.contact .line{position:absolute;left:100px;display:flex;align-items:center;gap:16px;font-size:15.5px;color:#222}
.contact .btn{position:absolute;left:98px;top:413px;width:140px;height:47px;border-radius:24px;background:var(--purple);color:#fff;font-size:13px;font-weight:700;display:flex;align-items:center;justify-content:center}
.map{position:absolute;left:0;top:0}

/* clients */
.clients{position:absolute;left:0;top:3300px;width:1200px;height:80px}
.client{position:absolute;top:30px;font-size:21px;font-weight:700;color:#6a6a6a;transform:translateX(-50%);white-space:nowrap}

/* footer */
.footer{position:absolute;left:0;top:3460px;width:1200px;height:426px;background:var(--footer);color:#fff;font-family:"Poppins",sans-serif}
.fcol{position:absolute;top:70px}
.fcol h4{font-size:21px;font-weight:600;margin-bottom:10px}
.fcol ul{list-style:none}
.fcol li{font-size:14.5px;line-height:30.5px;display:flex;align-items:center;gap:13px}
.news p{font-size:14.5px;line-height:31px;width:290px;margin-top:2px}
.news .email{margin-top:8px;width:270px;border-bottom:1px solid #fff;padding:4px 3px 8px;font-size:14px}
.news .btn{margin-top:22px;margin-left:7px;width:145px;height:50px;border-radius:25px;background:var(--purple);display:flex;align-items:center;justify-content:center;font-size:17px;font-weight:600}
.footer .rule{position:absolute;left:98px;top:356px;width:1004px;height:1px;background:#888}
.footer .copy{position:absolute;left:0;width:1200px;top:383px;text-align:center;font-size:15.5px;font-weight:500}
</style>
</head>
<body>

<header class="site-header">
  <div class="brand"><span class="brand-mark"></span><span class="brand-name">BRW</span></div>
  <div class="pill pill-phone">
    <svg width="15" height="15" viewBox="0 0 24 24" fill="#fff"><path d="M6.6 10.8a15.1 15.1 0 0 0 6.6 6.6l2.2-2.2a1 1 0 0 1 1-.25 11.4 11.4 0 0 0 3.6.57 1 1 0 0 1 1 1V20a1 1 0 0 1-1 1A17 17 0 0 1 3 4a1 1 0 0 1 1-1h3.5a1 1 0 0 1 1 1c0 1.25.2 2.45.57 3.57a1 1 0 0 1-.25 1z"/></svg>
    1300 555 014
  </div>
  <div class="pill pill-quote">REQUEST A QUOTE</div>
  <svg class="nav-bar" width="918" height="52" viewBox="0 0 918 52">
    <polygon points="6,52 34,0 44,0 16,52" fill="var(--ink)"/>
    <polygon points="24,52 52,0 918,0 918,52" fill="var(--purple)"/>
  </svg>
  <nav class="nav" style="left:356px">
    <span class="active">HOME</span><span>ABOUT US</span><span>PLANT HIRE</span><span>MAJOR PROJECT SNAPSHOT</span><span>POLICIES</span><span>JOBS</span><span>CONTACT US</span>
  </nav>
</header>

<section class="hero" role="img" aria-label="Orange excavator digging on a dusty construction site under a blue sky">
  <h1>BRW HEAVY<br>EQUIPMENT HIRE</h1>
  <div class="rule"></div>
  <p>Committed to superior quality plant hire services.</p>
  <div class="btn">GET STARTED</div>
  <svg class="scroll-cue" width="22" height="30" viewBox="0 0 22 30"><rect x="1.5" y="1.5" width="19" height="27" rx="9.5" fill="none" stroke="#fff" stroke-width="2"/><line x1="11" y1="7" x2="11" y2="13" stroke="#fff" stroke-width="2"/></svg>
</section>

<section>
  <div class="section-title" style="top:742px">
    <div class="ghost">WHO WE ARE</div>
    <h2 style="top:34px">WHO WE ARE</h2>
    <div class="bar" style="top:80px"></div>
  </div>
  <div class="features">
    <div class="feature" style="left:72px">
      <div class="ico" style="background:var(--purple)"><svg width="52" height="52" viewBox="0 0 52 52" fill="none" stroke="#fff" stroke-width="2"><circle cx="26" cy="22" r="5"/><circle cx="14" cy="27" r="4"/><circle cx="38" cy="27" r="4"/><path d="M17 44a9 9 0 0 1 18 0M6 44a8 8 0 0 1 12-6M46 44a8 8 0 0 0-12-6"/><path d="M26 6l1.5 3 3 .5-2.2 2 .6 3-2.9-1.5-2.9 1.5.6-3-2.2-2 3-.5z"/></svg></div>
      <p>20+ YEARS OF<br>EXPERIENCE</p>
    </div>
    <div class="feature" style="left:290px">
      <div class="ico" style="background:#111"><svg width="56" height="40" viewBox="0 0 56 40" fill="none" stroke="#fff" stroke-width="2"><rect x="8" y="8" width="18" height="14"/><circle cx="14" cy="30" r="7"/><circle cx="40" cy="32" r="5"/><path d="M26 22h22v6M2 24h6"/></svg></div>
      <p>MACHINES IN<br>FLEET</p>
    </div>
    <div class="feature" style="left:511px">
      <div class="ico" style="background:var(--purple)"><svg width="52" height="52" viewBox="0 0 52 52" fill="none" stroke="#fff" stroke-width="2"><path d="M6 46V18L26 6l20 12v28"/><rect x="16" y="28" width="20" height="14"/><circle cx="20" cy="44" r="2"/><circle cx="32" cy="44" r="2"/></svg></div>
      <p>ONE OF QLD'S<br>LARGEST SUPPLIERS</p>
    </div>
    <div class="feature" style="left:727px">
      <div class="ico" style="background:#111"><svg width="52" height="52" viewBox="0 0 52 52" fill="none" stroke="#fff" stroke-width="2"><circle cx="22" cy="22" r="9"/><path d="M10 24a12 12 0 0 1 24 0M8 44c2-8 8-12 14-12s12 4 14 12"/><rect x="32" y="8" width="14" height="10" rx="2"/></svg></div>
      <p>ONSITE<br>SERVICING</p>
    </div>
    <div class="feature" style="left:929px">
      <div class="ico" style="background:var(--purple)"><svg width="52" height="52" viewBox="0 0 52 52" fill="none" stroke="#fff" stroke-width="2"><rect x="6" y="12" width="40" height="28" rx="2"/><circle cx="26" cy="26" r="5"/><circle cx="14" cy="26" r="3"/><circle cx="38" cy="26" r="3"/><path d="M6 18h40M6 34h40"/></svg></div>
      <p>CUSTOM MACHINE<br>ATTACHMENTS</p>
    </div>
  </div>
</section>

<section class="about">
  <div class="about-photo" role="img" aria-label="Yellow graders and earthmoving machines parked on a gravel yard"></div>
  <svg class="about-ring" width="430" height="420" viewBox="0 0 430 420"><path d="M230 2 A205 205 0 0 1 215 412" fill="none" stroke="#c8bde0" stroke-width="2"/><path d="M232 4 A205 205 0 0 1 214 410 A200 200 0 0 0 232 4Z" fill="#5a3f8f"/></svg>
  <div class="about-text">
    <div class="ghost">ABOUT US</div>
    <h2>ABOUT US</h2>
    <div class="bar"></div>
    <p>Brackenridge Works Heavy Equipment Hire specialise in the hire of heavy earthmoving, mining and construction machines with specialised attachments and tooling. Our array of machines and attachments is second to none, and we have one of the largest hire fleets available in South East Queensland.</p>
    <p style="margin-top:28px">If its plant hire you require, then Brackenridge Works Resources, or BRW as the local's call us – should be the first call you make. Wet or dry hire, we provide excellent operators and quality machines across all makes and models to guarantee you maximum up-time.</p>
    <div class="btn">READ MORE</div>
  </div>
</section>

<section>
  <div class="section-title" style="top:1770px">
    <div class="ghost">OUR SERVICES</div>
    <h2 style="top:30px">OUR SERVICES</h2>
    <div class="bar" style="top:78px"></div>
  </div>
  <div class="card" style="left:100px">
    <div class="img" role="img" aria-label="Orange excavator working behind a site fence" style="background:linear-gradient(180deg,#8fb0d8 0%,#c7c2b8 50%,#8a7d6e 100%)"></div>
    <h3>EXCAVATORS</h3>
    <div class="arrow"><svg width="20" height="10" viewBox="0 0 20 10"><path d="M0 5h18M14 1l4 4-4 4" stroke="#fff" stroke-width="1.6" fill="none"/></svg></div>
    <div style="height:25px"></div>
  </div>
  <div class="card open" style="left:447px">
    <div class="img" role="img" aria-label="Yellow bulldozer on a dirt yard" style="background:linear-gradient(180deg,#9cb7cf 0%,#c9b27a 45%,#b08a3e 70%,#6c6458 100%)"></div>
    <h3>DOZERS FOR HIRE</h3>
    <p>Bulldozers of all sizes available for hire from the best manufacturers<br>The most prolific brands of dozer manufacturers are Ridgeline &amp; Koravin we have both machine brands available for hire based on your preference</p>
    <span class="more">READ MORE</span>
  </div>
  <div class="card" style="left:793px">
    <div class="img" role="img" aria-label="Yellow motor grader parked on a paved lot" style="background:linear-gradient(180deg,#7ea6d6 0%,#c4d3e2 45%,#b99a4c 70%,#6f6f6f 100%)"></div>
    <h3>GRADERS HIRE</h3>
    <div class="arrow"><svg width="20" height="10" viewBox="0 0 20 10"><path d="M0 5h18M14 1l4 4-4 4" stroke="#fff" stroke-width="1.6" fill="none"/></svg></div>
    <div style="height:25px"></div>
  </div>
  <div class="view-more">VIEW MORE</div>
</section>

<section class="contact">
  <svg class="map" width="1200" height="602" viewBox="0 0 1200 602">
    <path d="M640 0 C520 120 520 460 760 602 L1200 602 L1200 0Z" fill="var(--purple)"/>
    <path d="M698 0 C575 130 585 470 790 602 L1200 602 L1200 0Z" fill="#e7ebe7" role="img" aria-label="Street map showing the depot location"/>
  </svg>
  <h2>CONTACT US TODAY FOR A<br>FREE QUOTE</h2>
  <p class="lead">We deliver training throughout QLD but our primary training location is in EMERALD.</p>
  <div class="line" style="top:313px">
    <svg width="14" height="18" viewBox="0 0 14 18" fill="var(--purple)"><path d="M7 0a7 7 0 0 0-7 7c0 5 7 11 7 11s7-6 7-11a7 7 0 0 0-7-7zm0 9.5A2.5 2.5 0 1 1 7 4.5a2.5 2.5 0 0 1 0 5z"/></svg>
    18 Kestrel Rd, Brightvale QLD 4209
  </div>
  <div class="line" style="top:358px">
    <svg width="17" height="17" viewBox="0 0 24 24" fill="var(--purple)"><path d="M6.6 10.8a15.1 15.1 0 0 0 6.6 6.6l2.2-2.2a1 1 0 0 1 1-.25 11.4 11.4 0 0 0 3.6.57 1 1 0 0 1 1 1V20a1 1 0 0 1-1 1A17 17 0 0 1 3 4a1 1 0 0 1 1-1h3.5a1 1 0 0 1 1 1c0 1.25.2 2.45.57 3.57a1 1 0 0 1-.25 1z"/></svg>
    1300 555 014
  </div>
  <div class="btn">GET A QUOTE</div>
</section>

<section>
  <div class="section-title" style="top:3198px">
    <div class="ghost">OUR CLIENTS</div>
    <h2 style="top:30px">OUR CLIENTS</h2>
    <div class="bar" style="top:78px"></div>
  </div>
  <div class="clients">
    <svg class="abs" style="left:30px;top:22px" width="26" height="46" viewBox="0 0 26 46"><path d="M24 2L3 23l21 21" fill="none" stroke="#111" stroke-width="3"/></svg>
    <span class="client" style="left:164px">Harlow Civil</span>
    <span class="client" style="left:310px">Vantra</span>
    <span class="client" style="left:457px">Merridge</span>
    <span class="client" style="left:603px">Oakfield</span>
    <span class="client" style="left:750px">Kelbrook</span>
    <span class="client" style="left:895px">Tallis</span>
    <span class="client" style="left:1040px">Corvane</span>
    <svg class="abs" style="left:1143px;top:22px" width="26" height="46" viewBox="0 0 26 46"><path d="M2 2l21 21L2 44" fill="none" stroke="#111" stroke-width="3"/></svg>
  </div>
</section>

<footer class="footer">
  <div class="fcol" style="left:97px">
    <h4>Quick Links</h4>
    <ul>
      <li><svg width="14" height="12" viewBox="0 0 14 12"><path d="M0 6h12M7 1l5 5-5 5" stroke="#fff" stroke-width="2.4" fill="none"/></svg>Home</li>
      <li><svg width="14" height="12" viewBox="0 0 14 12"><path d="M0 6h12M7 1l5 5-5 5" stroke="#fff" stroke-width="2.4" fill="none"/></svg>About us</li>
      <li><svg width="14" height="12" viewBox="0 0 14 12"><path d="M0 6h12M7 1l5 5-5 5" stroke="#fff" stroke-width="2.4" fill="none"/></svg>Machine Operator Jobs</li>
      <li><svg width="14" height="12" viewBox="0 0 14 12"><path d="M0 6h12M7 1l5 5-5 5" stroke="#fff" stroke-width="2.4" fill="none"/></svg>Plant Hire</li>
      <li><svg width="14" height="12" viewBox="0 0 14 12"><path d="M0 6h12M7 1l5 5-5 5" stroke="#fff" stroke-width="2.4" fill="none"/></svg>Attachments Hire</li>
      <li><svg width="14" height="12" viewBox="0 0 14 12"><path d="M0 6h12M7 1l5 5-5 5" stroke="#fff" stroke-width="2.4" fill="none"/></svg>Policies</li>
    </ul>
  </div>
  <div class="fcol" style="left:343px">
    <h4>Other Links</h4>
    <ul>
      <li><svg width="14" height="12" viewBox="0 0 14 12"><path d="M0 6h12M7 1l5 5-5 5" stroke="#fff" stroke-width="2.4" fill="none"/></svg>Articulated Dump Trucks Hire</li>
      <li><svg width="14" height="12" viewBox="0 0 14 12"><path d="M0 6h12M7 1l5 5-5 5" stroke="#fff" stroke-width="2.4" fill="none"/></svg>Dozer Hire</li>
      <li><svg width="14" height="12" viewBox="0 0 14 12"><path d="M0 6h12M7 1l5 5-5 5" stroke="#fff" stroke-width="2.4" fill="none"/></svg>Excavator Diggers Hire</li>
      <li><svg width="14" height="12" viewBox="0 0 14 12"><path d="M0 6h12M7 1l5 5-5 5" stroke="#fff" stroke-width="2.4" fill="none"/></svg>Grader Hire</li>
      <li><svg width="14" height="12" viewBox="0 0 14 12"><path d="M0 6h12M7 1l5 5-5 5" stroke="#fff" stroke-width="2.4" fill="none"/></svg>Attachments Hire</li>
    </ul>
  </div>
  <div class="fcol" style="left:636px">
    <h4>Other Links</h4>
    <ul>
      <li><svg width="14" height="12" viewBox="0 0 14 12"><path d="M0 6h12M7 1l5 5-5 5" stroke="#fff" stroke-width="2.4" fill="none"/></svg>Backhoe Hire</li>
      <li><svg width="14" height="12" viewBox="0 0 14 12"><path d="M0 6h12M7 1l5 5-5 5" stroke="#fff" stroke-width="2.4" fill="none"/></svg>Compactors Hire</li>
      <li><svg width="14" height="12" viewBox="0 0 14 12"><path d="M0 6h12M7 1l5 5-5 5" stroke="#fff" stroke-width="2.4" fill="none"/></svg>Loader Hire</li>
      <li><svg width="14" height="12" viewBox="0 0 14 12"><path d="M0 6h12M7 1l5 5-5 5" stroke="#fff" stroke-width="2.4" fill="none"/></svg>Skid Steer Hire</li>
      <li><svg width="14" height="12" viewBox="0 0 14 12"><path d="M0 6h12M7 1l5 5-5 5" stroke="#fff" stroke-width="2.4" fill="none"/></svg>Water Cart Hire</li>
    </ul>
  </div>
  <div class="fcol news" style="left:828px">
    <h4>Sign Up To Our Newsletter</h4>
    <p>Lorem ipsum dolor sit amet,consectetur adipiscing elit,adipiscing elit.</p>
    <div class="email">Email</div>
    <div class="btn">Subscribe</div>
  </div>
  <div class="rule"></div>
  <div class="copy">Copyrights@2024.BRW.All Rights Reserved</div>
</footer>

</body>
</html>
```